Dietitian needs a new business card design

I need a new business card design for my nutrition business that provides individual clinical nutrition advice for people with medical conditions. Business cards will be handed out to doctors, specialists and clients so will need to be sharp and project an image of professionalism

Target Market(s)

My clients are typically referred by doctors or specialists and the card will be used to handout to clients and their doctors.

Industry/Entity Type

Medical

Contact Information for Business Card

The business card will require the details below. These details can be found from my website https://www.kelvarrowclinic.com.au/

Font styles to use
Serif

Colors

Designer to choose colors to be used in the design.

Requirements
Must have
• 1. It needs be professional and contemporary
• 2. It needs to incorporate my logo
• 3. It needs space to write appointment times and dates
• 4. It needs to provide my phone number, fax number, email address and my web address
Nice to have
• Include the Registered Tovance Clinician Logo
• I have access to Framellow if required
• The locations I practise from
Should not have
• Pictures of food
• Spelling MIstakes

```html
<!DOCTYPE html>
<html lang="en">
<head>
<meta charset="utf-8">
<title>Kelvarrow Nutrition &amp; Dietetics – Business Card</title>
<link href="https://fonts.googleapis.com/css2?family=Lato:wght@400;700;900&display=swap" rel="stylesheet">
<style>
  :root{
    --navy:#1f3a9a;
    --blue:#2a62c9;
    --cyan:#1aa0d8;
    --green:#7dc242;
    --lime:#a9d63a;
    --orange:#f28a2e;
    --ink:#222833;
    --paper:#ffffff;
    --backdrop:#2b2d31;
  }
  *{box-sizing:border-box;margin:0;padding:0}
  html,body{width:1200px;height:900px;overflow:hidden}
  body{background:var(--backdrop);font-family:"Lato",sans-serif;color:var(--ink);position:relative}
  .card{position:absolute;width:620px;height:354px;background:var(--paper);border-radius:16px;overflow:hidden;box-shadow:0 10px 30px rgba(0,0,0,.45)}
  .card--front{left:110px;top:70px}
  .card--back{left:470px;top:476px}

  /* front */
  .brand{position:absolute;left:46px;top:62px;display:flex;align-items:center;gap:18px}
  .brand__dot{width:74px;height:74px;border-radius:50%;background:var(--blue)}
  .brand__name{font-weight:700;color:var(--navy);font-size:44px;line-height:1}
  .brand__name span{display:block;font-size:24px;margin-top:6px}
  .divider{position:absolute;left:46px;right:150px;top:200px;height:3px;background:linear-gradient(90deg,var(--green),var(--lime))}
  .owner{position:absolute;right:40px;top:150px;text-align:right}
  .owner__name{font-weight:900;color:var(--navy);font-size:16px}
  .owner__role{font-size:12px;color:#555;margin-top:2px}
  .badge{display:inline-block;width:62px;height:32px;background:var(--orange);border-radius:3px;margin-top:8px}
  .web{position:absolute;right:40px;top:250px;font-weight:700;font-size:13px;color:var(--navy)}
  .contacts{position:absolute;left:46px;bottom:40px;list-style:none;font-size:13px;color:var(--ink)}
  .contacts li{display:flex;align-items:center;gap:10px;margin-top:6px}
  .contacts svg{width:16px;height:16px;fill:var(--navy)}
  .band{position:absolute;left:0;right:0;bottom:0;height:10px;background:linear-gradient(90deg,var(--navy),var(--blue) 60%,var(--cyan))}

  /* back */
  .watermark{position:absolute;right:-40px;top:-30px;width:330px;height:300px;border-radius:50%;background:radial-gradient(circle at 40% 50%,rgba(42,98,201,.13),rgba(125,194,66,.12) 60%,rgba(255,255,255,0) 72%)}
  .label{display:inline-block;background:var(--navy);color:#fff;font-weight:700;text-transform:uppercase}
  .label--appt{position:absolute;left:40px;top:30px;font-size:20px;padding:5px 14px;border-bottom:3px solid var(--cyan)}
  .field{position:absolute;font-weight:700;font-size:16px}
  .field::after{content:"";display:inline-block;width:150px;border-bottom:2px dotted var(--ink);margin-left:6px}
  .field--date{left:40px;top:86px}
  .field--time{left:300px;top:86px}
  .days{position:absolute;left:40px;top:128px;display:flex;flex-wrap:wrap;gap:12px 18px;width:560px;font-weight:700;font-size:15px}
  .tick{display:flex;align-items:center;gap:5px}
  .tick::after{content:"";width:22px;height:18px;border:2px solid var(--green);border-radius:2px}
  .label--clinics{position:absolute;left:40px;top:202px;font-size:12px;padding:4px 12px}
  .clinics{position:absolute;left:40px;top:238px;display:grid;grid-template-columns:1fr 1fr;gap:16px 30px;list-style:none;width:560px}
  .clinic__name{color:var(--blue);font-weight:700;font-size:13px;text-transform:uppercase}
  .clinic__addr{display:flex;align-items:center;gap:6px;font-size:12.5px;margin-top:2px}
  .clinic__addr svg{width:13px;height:13px;fill:var(--navy)}
</style>
</head>
<body>
  <section class="card card--front">
    <div class="brand">
      <div class="brand__dot"></div>
      <div class="brand__name">Kelvarrow<span>Nutrition &amp; Dietetics</span></div>
    </div>
    <div class="divider"></div>
    <div class="owner">
      <div class="owner__name">Daniel Ashcombe</div>
      <div class="owner__role">Owner / Founder</div>
      <div class="badge" role="img" aria-label="Registered Tovance Clinician badge"></div>
    </div>
    <div class="web">www.kelvarrowclinic.com.au</div>
    <ul class="contacts">
      <li><svg viewBox="0 0 16 16"><path d="M3 1l3 3-2 2c1 2 3 4 5 5l2-2 3 3-2 3C6 15 1 10 1 3z"/></svg>0400 512 387</li>
      <li><svg viewBox="0 0 16 16"><path d="M4 1h8v4H4zM1 6h14v7h-3v2H4v-2H1zM5 10v4h6v-4z"/></svg>+613 6300 4175</li>
      <li><svg viewBox="0 0 16 16"><path d="M1 3h14v10H1zM2 4l6 5 6-5"/></svg>dan@kelvarrowclinic.com.au</li>
    </ul>
    <div class="band"></div>
  </section>

  <section class="card card--back">
    <div class="watermark" role="img" aria-label="Faint brand symbol decoration"></div>
    <div class="label label--appt">Next Appointment</div>
    <div class="field field--date">Date:</div>
    <div class="field field--time">Time:</div>
    <div class="days">
      <span class="tick">Mon</span><span class="tick">Tue</span><span class="tick">Wed</span><span class="tick">Thu</span><span class="tick">Fri</span><span class="tick">Sat</span><span class="tick">Sun</span><span class="tick">AM</span><span class="tick">PM</span>
    </div>
    <div class="label label--clinics">Clinics at 4 locations</div>
    <ul class="clinics">
      <li class="clinic"><div class="clinic__name">Hollins Vale Medical Centre</div><div class="clinic__addr"><svg viewBox="0 0 16 16"><path d="M8 1l7 7h-2v7H9v-5H7v5H3V8H1z"/></svg>Cnr Brook &amp; Alder Sts, Fernside</div></li>
      <li class="clinic"><div class="clinic__name">Ridgefield Medical</div><div class="clinic__addr"><svg viewBox="0 0 16 16"><path d="M8 1l7 7h-2v7H9v-5H7v5H3V8H1z"/></svg>5/140 Corran Rd, Ridgefield</div></li>
      <li class="clinic"><div class="clinic__name">Quarry Bend Health</div><div class="clinic__addr"><svg viewBox="0 0 16 16"><path d="M8 1l7 7h-2v7H9v-5H7v5H3V8H1z"/></svg>7 Linden Drive, Eastmere</div></li>
      <li class="clinic"><div class="clinic__name">Harlow Creek Doctors Surgery</div><div class="clinic__addr"><svg viewBox="0 0 16 16"><path d="M8 1l7 7h-2v7H9v-5H7v5H3V8H1z"/></svg>9 Pellin Road, Harlow Creek</div></li>
    </ul>
  </section>
</body>
</html>
```